Quiet Harbor Podcast W/ Dr. Gus Penn

Podcast Cover Art. I am in search of a re-design for my existing podcast. We have over 100 episodes, but I want to change the name to Quiet Harbor Podcast With Dr. Gus Penn. I'm open to any ideas, and have attached source file image to use. ( note: NO brain images please).

```html
<!DOCTYPE html>
<html lang="en">
<head>
<meta charset="UTF-8">
<title>Quiet Harbor Podcast With Dr. Gus Penn</title>
<link href="https://fonts.googleapis.com/css2?family=Bebas+Neue&family=Poppins:wght@700&family=Allura&display=swap" rel="stylesheet">
<style>
  :root {
    --cover-top: #bf3f2c;
    --cover-bottom: #d44d32;
    --sun: #f4c27c;
    --title-white: #ffffff;
    --name-gold: #f3c27e;
    --art-warm: #e8663f;
    --art-deep: #c9432f;
  }
  html, body {
    margin: 0;
    padding: 0;
    width: 1200px;
    height: 1200px;
    overflow: hidden;
  }
  .cover {
    position: relative;
    width: 1200px;
    height: 1200px;
    background: linear-gradient(180deg, var(--cover-top) 0%, var(--cover-bottom) 65%);
    overflow: hidden;
  }
  .sun-disc {
    position: absolute;
    left: 300px;
    top: 150px;
    width: 590px;
    height: 590px;
    border-radius: 50%;
    background: var(--sun);
  }
  .host-portrait {
    position: absolute;
    left: 280px;
    top: 80px;
    width: 630px;
    height: 800px;
    border-radius: 315px 315px 0 0;
    background: linear-gradient(180deg, rgba(232,102,63,0) 0%, rgba(232,102,63,0) 40%, var(--art-warm) 62%, var(--art-deep) 100%);
  }
  .title-words {
    position: absolute;
    left: 0;
    top: 0;
    width: 1200px;
    height: 1200px;
  }
  .title-word {
    font-family: "Bebas Neue", "Oswald", sans-serif;
    fill: var(--title-white);
    font-size: 330px;
  }
  .tagline {
    position: absolute;
    left: 62px;
    top: 880px;
    margin: 0;
    font-family: "Allura", cursive;
    font-size: 92px;
    color: var(--title-white);
    line-height: 1;
  }
  .host-name {
    position: absolute;
    left: 48px;
    top: 975px;
    margin: 0;
    font-family: "Poppins", sans-serif;
    font-weight: 700;
    font-size: 112px;
    letter-spacing: -2px;
    color: var(--name-gold);
    line-height: 1.1;
    white-space: nowrap;
  }
</style>
</head>
<body>
  <main class="cover">
    <div class="sun-disc"></div>
    <div class="host-portrait" role="img" aria-label="Illustrated portrait of the host in a checked orange blazer"></div>
    <svg class="title-words" viewBox="0 0 1200 1200" role="img" aria-label="Quiet Harbor">
      <text class="title-word" transform="translate(272,850) rotate(-90)" textLength="760" lengthAdjust="spacingAndGlyphs">QUIET</text>
      <text class="title-word" transform="translate(932,90) rotate(90)" textLength="1080" lengthAdjust="spacingAndGlyphs">HARBOR</text>
    </svg>
    <p class="tagline">Podcast With</p>
    <p class="host-name">Dr. Gus Penn</p>
  </main>
</body>
</html>
```